Business Card Design

Looking for a professional looking business card for a carpentry/construction business that deals with renovations, extensions, homes, and anything carpentry based in Northern Australia. Would like to incorporate the attached logo with backgrounds of white, grey or maybe a close up of timber/wood grain. Thanks

Industry/Entity Type

Carpentry

Contact Information for Business Card

Dean Pollard, Owner, Po Box 2946 Katherine NT 0851, dean-pollard@tallmail.example, 0461907243, Builders Number: 392417CR

Requirements
Should not have
• Power tools/hand tools related to carpentry

```html
<!DOCTYPE html>
<html lang="en">
<head>
<meta charset="utf-8">
<title>Pollard Carpentry – Business Card</title>
<link href="https://fonts.googleapis.com/css2?family=Arimo:ital,wght@0,400;1,400&family=Ubuntu:wght@700&display=swap" rel="stylesheet">
<style>
  :root {
    --backdrop: #e6e7ea;
    --card-white: #f4f4f5;
    --brand-blue: #2b48a8;
    --ink: #2d2f33;
    --ink-soft: #55585e;
    --on-blue: #ffffff;
  }
  * { box-sizing: border-box; margin: 0; padding: 0; }
  html, body {
    width: 1200px; height: 873px; overflow: hidden;
    background: var(--backdrop);
  }
  .sheet {
    width: 1200px; height: 873px;
    display: flex; align-items: center; justify-content: center; gap: 60px;
  }
  .card {
    position: relative;
    width: 520px; height: 300px;
    background: var(--card-white);
    border-radius: 4px;
    box-shadow: 0 10px 24px rgba(0,0,0,0.18);
    overflow: hidden;
  }
  .card-shape { position: absolute; inset: 0; width: 100%; height: 100%; }
  .card-shape polygon { fill: var(--brand-blue); }

  .brand {
    position: absolute;
    display: flex; align-items: center; gap: 10px;
    font-family: "Ubuntu", sans-serif; font-weight: 700;
    white-space: nowrap;
  }
  .brand-mark { display: block; width: 14px; height: 14px; }
  .brand--front { right: 34px; top: 122px; font-size: 34px; color: var(--brand-blue); }
  .brand--front .brand-mark { background: var(--brand-blue); }
  .brand--back { right: 24px; bottom: 26px; font-size: 22px; color: var(--on-blue); }
  .brand--back .brand-mark { width: 10px; height: 10px; background: var(--on-blue); }

  .contact {
    position: absolute; left: 34px; top: 30px;
    font-family: "Arimo", sans-serif; color: var(--ink-soft);
    font-size: 13px; line-height: 1.55;
  }
  .contact-name { font-size: 24px; color: var(--ink); line-height: 1.1; }
  .contact-role { font-style: italic; font-size: 14px; margin-bottom: 8px; }
  .contact-lines { list-style: none; }
</style>
</head>
<body>
<main class="sheet">
  <section class="card card--back" aria-label="Card back with contact details">
    <svg class="card-shape" viewBox="0 0 520 300" aria-hidden="true">
      <polygon points="0,300 0,228 40,206 78,236 190,200 300,162 410,124 520,160 520,300"/>
    </svg>
    <div class="contact">
      <p class="contact-name">Dean Pollard</p>
      <p class="contact-role">Owner</p>
      <ul class="contact-lines">
        <li>Po Box 2946</li>
        <li>Bramwell NT 0854</li>
        <li>dean-pollard@tallmail.example</li>
        <li>0461907243</li>
        <li>BN: 392417CR</li>
      </ul>
    </div>
    <p class="brand brand--back"><span class="brand-mark"></span>Pollard Carpentry</p>
  </section>

  <section class="card card--front" aria-label="Card front with company name">
    <svg class="card-shape" viewBox="0 0 520 300" aria-hidden="true">
      <polygon points="0,0 150,0 108,62 118,112 150,300 0,300"/>
    </svg>
    <p class="brand brand--front"><span class="brand-mark"></span>Pollard Carpentry</p>
  </section>
</main>
</body>
</html>
```